Crestwell Advisory Services

I'm looking to create a flyer for my business to provide a consultant service. I will be providing the following below
Launch Your Business Today for only $150
(state fee not included)
Business Formation includes:
*Limited liability Corporation (LLC)
*Halvers and Quint Number
*FEIN
*Operation Agreement for partnership LLCs (For 2 or more member(s)
*Commercial Activity license (If needed for your Business )
*Same -day turnaround service with documents
Schedule your Appointment today
Call or text:318-472-6051
Email:MoralesCapitalCircle@fernmail.net
Target Market(s)
I want the flyer to attract people who wants to start a business but doesn’t know where to start. I want the flyer to stand out form the other consultant businesses.
Industry/Entity Type
Consultant
Requirements
Must have
- The State fee not included should be in small print
Highlight the price or service
Highlight the phrase "launch you business today"
Nice to have
- Different samples of colors, a variety
Should not have
- should not be all one color

```html
<!DOCTYPE html>
<html lang="en">
<head>
<meta charset="utf-8">
<title>Crestwell Advisory Services – Launch Your Business Today</title>
<link href="https://fonts.googleapis.com/css2?family=Outfit:wght@300;400;600;700;800&family=Montserrat:wght@700;800&display=swap" rel="stylesheet">
<style>
  :root {
    --ink: #21232b;
    --white: #ffffff;
    --sky: #a3c6e8;
    --brand-blue: #86acd8;
    --orange: #f48a4b;
    --red: #e9474f;
    --gold: #f9ae3b;
    --teal: rgba(52, 176, 178, 0.78);
    --magenta-top: rgba(183, 92, 176, 0.9);
    --magenta-bottom: #9a4a77;
    --green: #2bae85;
    --phone-blue: #6a95d2;
    --rule: #e58a3c;
  }
  * { box-sizing: border-box; margin: 0; padding: 0; }
  html, body { width: 849px; height: 1200px; overflow: hidden; background: var(--ink); }
  .flyer {
    position: relative; width: 849px; height: 1200px; overflow: hidden;
    background: var(--ink); font-family: "Outfit", sans-serif; color: var(--white);
  }
  .header { position: absolute; left: 0; top: 0; width: 849px; height: 241px; background: var(--ink); }
  .brand-square { position: absolute; left: 71px; top: 53px; width: 176px; height: 142px; background: var(--sky); }
  .brand-name {
    position: absolute; left: 260px; top: 82px; width: 330px;
    font-family: "Outfit", sans-serif; font-weight: 700; color: var(--brand-blue);
  }
  .brand-name-main { display: block; font-size: 47px; line-height: 1; letter-spacing: 0.5px; }
  .brand-name-sub { display: block; margin-top: 10px; padding-left: 46px; font-size: 14px; line-height: 1; letter-spacing: 4.6px; }
  .hero-photo {
    position: absolute; left: 0; top: 241px; width: 849px; height: 737px;
    background:
      radial-gradient(ellipse at 75% 25%, rgba(70,170,225,0.55), transparent 60%),
      radial-gradient(ellipse at 30% 60%, rgba(40,150,210,0.45), transparent 55%),
      linear-gradient(160deg, #1f4aa6 0%, #2a78c8 45%, #1d57b0 75%, #173c8e 100%);
  }
  .headline { position: absolute; left: 66px; top: 296px; font-weight: 700; }
  .headline-launch {
    position: absolute; left: 0; top: 0; font-weight: 600; font-size: 79px; line-height: 1;
    letter-spacing: -1.5px; color: var(--white); white-space: nowrap;
  }
  .headline-business {
    position: absolute; left: 0; top: 78px; font-size: 141px; line-height: 1;
    letter-spacing: -1.5px; color: var(--orange); white-space: nowrap;
    text-shadow: 0 3px 8px rgba(0,0,0,0.25);
  }
  .headline-today {
    position: absolute; left: 2px; top: 205px; font-size: 101px; line-height: 1;
    letter-spacing: -1px; color: var(--red); white-space: nowrap;
  }
  .price-box {
    position: absolute; left: 68px; top: 626px; width: 328px; height: 272px;
    background: var(--teal); border-top-left-radius: 42px; text-align: center;
  }
  .price-label {
    position: absolute; left: 0; right: 0; top: 31px; font-family: "Montserrat", sans-serif;
    font-weight: 800; font-size: 22px; letter-spacing: 6px; padding-left: 6px;
  }
  .price-amount { position: absolute; left: 20px; top: 66px; display: flex; align-items: flex-start; }
  .price-currency { font-weight: 400; font-size: 50px; line-height: 1; margin-top: 8px; }
  .price-value { font-weight: 700; font-size: 168px; line-height: 0.9; letter-spacing: -6px; margin-left: 4px; }
  .price-note { position: absolute; left: 0; right: 0; top: 218px; font-weight: 300; font-size: 21px; }
  .includes-panel {
    position: absolute; left: 427px; top: 513px; width: 348px; height: 638px;
    background: linear-gradient(180deg, var(--magenta-top) 0%, rgba(165,80,150,0.92) 60%, var(--magenta-bottom) 100%);
    border-bottom-right-radius: 48px;
  }
  .includes-title {
    position: absolute; left: 26px; top: 40px; font-weight: 800; font-size: 48px; line-height: 52px;
    color: var(--gold); letter-spacing: 0.5px;
  }
  .includes-rule { position: absolute; left: 27px; top: 228px; width: 288px; height: 2px; background: var(--gold); }
  .includes-list {
    position: absolute; left: 28px; top: 266px; list-style: none; font-weight: 300; font-size: 18px;
    line-height: 21.3px; white-space: nowrap;
  }
  .includes-list li { position: relative; padding-left: 17px; margin-bottom: 14.3px; }
  .includes-list li::before {
    content: ""; position: absolute; left: 0; top: 8px; width: 6px; height: 6px; border-radius: 50%;
    background: var(--white);
  }
  .cta-box {
    position: absolute; left: 68px; top: 1041px; width: 313px; height: 61px;
    border: 1px solid var(--rule); border-top-right-radius: 22px;
    padding: 9px 0 0 14px; font-family: "Montserrat", sans-serif; font-weight: 800; font-size: 20px;
    line-height: 22px; letter-spacing: 2.2px; color: var(--green);
  }
  .contact { position: absolute; left: 82px; top: 1110px; font-weight: 400; font-size: 15.5px; line-height: 21px; }
  .contact-phone { font-weight: 600; font-size: 21px; color: var(--phone-blue); }
</style>
</head>
<body>
<main class="flyer">
  <header class="header">
    <div class="brand-square"></div>
    <div class="brand-name">
      <span class="brand-name-main">CRESTWELL</span>
      <span class="brand-name-sub">ADVISORY SERVICES</span>
    </div>
  </header>

  <div class="hero-photo" role="img" aria-label="Photo of business partners shaking hands over paperwork, in blue tones"></div>

  <h1 class="headline">
    <span class="headline-launch">Launch Your</span>
    <span class="headline-business">BUSINESS</span>
    <span class="headline-today">TODAY</span>
  </h1>

  <section class="price-box">
    <p class="price-label">FOR ONLY</p>
    <p class="price-amount"><span class="price-currency">$</span><span class="price-value">150</span></p>
    <p class="price-note">(state fee not included)</p>
  </section>

  <section class="includes-panel">
    <h2 class="includes-title">BUSINESS<br>FORMATION<br>INCLUDES:</h2>
    <div class="includes-rule"></div>
    <ul class="includes-list">
      <li>Limited Liability Company (LLC)</li>
      <li>Halvers and Quint Number</li>
      <li>FEIN<br>(Employer Identification Number)</li>
      <li>Operation Agreement for<br>partnership LLCs<br>(For 2 or more members)</li>
      <li>Commercial Activity license<br>(If needed for your LLC)</li>
      <li>Same-day turnaround service<br>with documents<br>(Depending on the state)</li>
    </ul>
  </section>

  <div class="cta-box">SCHEDULE YOUR<br>APPOINTMENT TODAY</div>

  <div class="contact">
    <p>Call or Text: <span class="contact-phone">318-472-6051</span></p>
    <p>Email: MoralesCapitalCircle@fernmail.net</p>
  </div>
</main>
</body>
</html>
```